Email Signature & Facebook Cover Design – Birchlane Study Centre

I’m looking for a clean, professional email signature and a matching Facebook cover photo for my tutoring business, Birchlane Study Centre.
The email signature needs to display properly across Outlook and iPhone without the image appearing as an attachment. It should include my logo and contact details and have a friendly but professional look suitable for an education business.
Details to include:
Moira Dunholt
Director & Lead Tutor
Birchlane Study Centre
hello@birchlanestudy.co.uk
www.birchlanestudy.co.uk
01632 418736
The Facebook cover should match the branding, feel professional and welcoming, and be optimised for desktop and mobile.

```html
<!DOCTYPE html>
<html lang="en">
<head>
<meta charset="utf-8">
<title>Birchlane Study Centre – Email Signature</title>
<link rel="stylesheet" href="https://fonts.googleapis.com/css2?family=Poppins:wght@400;500;600;800&display=swap">
<style>
  :root {
    --board: #272727;
    --card: #ffffff;
    --green: #48b96a;
    --ink: #3b3b3b;
    --ink-dark: #111111;
    --label: #3a3a3a;
  }
  * { margin: 0; padding: 0; box-sizing: border-box; }
  html, body { width: 1200px; height: 240px; overflow: hidden; background: var(--board); }
  body { font-family: "Poppins", sans-serif; position: relative; }

  .signature {
    position: absolute; left: 22px; top: 18px;
    width: 612px; height: 203px;
    background: var(--card); overflow: hidden;
  }

  .identity {
    position: absolute; left: 60px; top: 0; width: 164px; height: 100%;
    display: flex; flex-direction: column; align-items: center;
  }
  .brand-mark {
    margin-top: 36px; height: 96px;
    display: flex; align-items: center; gap: 8px;
  }
  .brand-mark .dot {
    width: 14px; height: 14px; border-radius: 50%;
    background: var(--green); flex: none;
  }
  .brand-mark .brand-name {
    font-weight: 800; font-size: 21px; line-height: 1.05;
    color: var(--ink-dark); letter-spacing: -0.3px;
  }
  .person-name {
    margin-top: 12px; width: 144px; height: 17px;
    background: var(--green); border-radius: 2px;
    color: #fff; font-weight: 800; font-size: 9.5px;
    letter-spacing: 0.42em; text-transform: uppercase;
    display: flex; align-items: center; justify-content: center;
    padding-left: 0.42em;
  }
  .person-role {
    margin-top: 7px; font-weight: 500; font-size: 8.5px;
    color: var(--ink); letter-spacing: 0.2px;
  }

  .divider {
    position: absolute; left: 260px; top: 28px;
    width: 2px; height: 149px; background: var(--green);
  }

  .company-band {
    position: absolute; left: 288px; top: 55px;
    width: 324px; height: 33px; background: var(--green);
    display: flex; align-items: center; padding-left: 18px;
  }
  .company-band h1 {
    color: #fff; font-weight: 800; font-size: 19.5px;
    letter-spacing: 0.2px; white-space: nowrap; line-height: 1;
  }

  .contacts { position: absolute; left: 310px; top: 98px; list-style: none; }
  .contacts li { display: flex; align-items: center; color: var(--ink); }
  .contacts .icon { width: 10px; height: 10px; margin-right: 18px; flex: none; }
  .contacts .phone { font-weight: 800; font-size: 17px; height: 28px; }
  .contacts .email, .contacts .web { font-weight: 500; font-size: 12px; height: 18px; }

  .board-label {
    position: absolute; left: 726px; top: 104px;
    font-weight: 800; font-size: 25px; line-height: 1;
    letter-spacing: 0.56em; color: var(--label); white-space: nowrap;
  }
</style>
</head>
<body>
  <section class="signature">
    <div class="identity">
      <div class="brand-mark">
        <span class="dot"></span>
        <span class="brand-name">Birchlane<br>Study Centre</span>
      </div>
      <div class="person-name">Moira Dunholt</div>
      <div class="person-role">DIRECTOR &amp; LEAD TUTOR</div>
    </div>

    <div class="divider"></div>

    <div class="company-band"><h1>BIRCHLANE STUDY CENTRE</h1></div>

    <ul class="contacts">
      <li class="phone">
        <svg class="icon" viewBox="0 0 24 24" aria-hidden="true"><path fill="#48b96a" d="M6.6 10.8c1.4 2.8 3.8 5.1 6.6 6.6l2.2-2.2c.3-.3.7-.4 1-.2 1.1.4 2.3.6 3.6.6.6 0 1 .4 1 1V20c0 .6-.4 1-1 1C10.6 21 3 13.4 3 4c0-.6.4-1 1-1h3.5c.6 0 1 .4 1 1 0 1.3.2 2.5.6 3.6.1.3 0 .7-.2 1z"/></svg>
        01632 418736
      </li>
      <li class="email">
        <svg class="icon" viewBox="0 0 24 24" aria-hidden="true"><rect x="2" y="5" width="20" height="14" fill="#48b96a"/><path d="M2 5l10 8 10-8M2 19l8-7M22 19l-8-7" stroke="#fff" stroke-width="1.6" fill="none"/></svg>
        hello@birchlanestudy.co.uk
      </li>
      <li class="web">
        <svg class="icon" viewBox="0 0 24 24" aria-hidden="true"><g fill="none" stroke="#48b96a" stroke-width="1.8"><circle cx="12" cy="12" r="10"/><ellipse cx="12" cy="12" rx="4.5" ry="10"/><path d="M2 12h20M4 6.5h16M4 17.5h16"/></g></svg>
        www.birchlanestudy.co.uk
      </li>
    </ul>
  </section>

  <div class="board-label">EMAIL SIGNATURE</div>
</body>
</html>
```